Personal Trainer Business Card

I need a business card using a logo I already have.
The logo is in uploaded files.
Card is to give to prospective clients that interested in health and beauty or already exercise. Would like logo on front or other abstract images and details on back.
Like modern design that also unique and eye catching rather than just generic fitness gym/fitness theme.

Target Market(s)

Main clients are trendy women aged 25-60.

Industry/Entity Type

Fitness

Contact Information for Business Card

Email: tom@tomharvecoaching.com

web: www.tomharvecoaching.com

mobile: 0493 257618

facebook: www.facebook.com/tomharvecoaching

Location is: Sunshine Coast

Font styles to use
Sans Serif

Colors
000000
1b1b1b
333333

Requirements
Must have
• Logo on front
• black background of sorts on front (fine if mixed with dark grey or abstract)
• White background on back.
Nice to have
• I would like the front side with the logo appearing on it with black background. Fine with alternative ideas and layout.
• Would like the front to be modern, professional and cool/interesting.
• Fine with abstract or modern design.
• Reverse of the card some white background with details on it
• (I like simple fonts).
• CAn use same font colour as in logo in places or what whatever
Should not have
• Avoiding use of cheap pics such as weights

```html
<!DOCTYPE html>
<html lang="en">
<head>
<meta charset="utf-8">
<title>Tom Harve Coaching – Business Card</title>
<link rel="stylesheet" href="https://fonts.googleapis.com/css2?family=Montserrat:wght@500;800&display=swap">
<style>
  :root {
    --stage: #ececec;
    --card-black: #1b1b1b;
    --card-white: #ffffff;
    --gold: #bf9b5a;
    --ink: #333333;
    --shadow: rgba(0, 0, 0, 0.12);
  }
  * { box-sizing: border-box; margin: 0; padding: 0; }
  html, body {
    width: 1200px;
    height: 900px;
    overflow: hidden;
    background: var(--stage);
    font-family: "Montserrat", Arial, sans-serif;
  }
  .stage {
    width: 1200px;
    height: 900px;
    display: flex;
    align-items: center;
    justify-content: center;
    gap: 60px;
  }
  .card {
    width: 510px;
    height: 310px;
    border-radius: 3px;
    box-shadow: 0 10px 30px var(--shadow);
    display: flex;
    flex-direction: column;
    align-items: center;
    justify-content: center;
  }
  .card--front { background: var(--card-black); }
  .card--back { background: var(--card-white); }

  .wordmark {
    color: var(--gold);
    font-weight: 800;
    text-align: center;
    text-transform: uppercase;
    line-height: 1;
  }
  .wordmark__name {
    display: block;
    font-size: 40px;
    letter-spacing: 1px;
  }
  .wordmark__trade {
    display: block;
    font-size: 15px;
    letter-spacing: 9px;
    margin-top: 8px;
    padding-left: 9px;
  }

  .social {
    margin-top: 34px;
    display: flex;
    flex-direction: column;
    align-items: center;
    gap: 6px;
    color: var(--gold);
    font-size: 11px;
    font-weight: 500;
  }
  .social__mark {
    width: 9px;
    height: 9px;
    background: var(--gold);
    border-radius: 1px;
  }

  .contact-icons {
    margin-top: 26px;
    display: flex;
    gap: 8px;
  }
  .contact-icons svg { width: 11px; height: 11px; }
  .contact-list {
    margin-top: 6px;
    list-style: none;
    text-align: center;
    color: var(--ink);
    font-size: 12px;
    font-weight: 500;
    line-height: 1.35;
  }
</style>
</head>
<body>
<main class="stage">
  <section class="card card--front" aria-label="Card front">
    <div class="wordmark">
      <span class="wordmark__name">Tom Harve</span>
      <span class="wordmark__trade">Coaching</span>
    </div>
    <div class="social">
      <span class="social__mark" aria-hidden="true"></span>
      <span class="social__handle">tomharvecoaching</span>
    </div>
  </section>

  <section class="card card--back" aria-label="Card back">
    <div class="wordmark">
      <span class="wordmark__name">Tom Harve</span>
      <span class="wordmark__trade">Coaching</span>
    </div>
    <div class="contact-icons" aria-hidden="true">
      <svg viewBox="0 0 12 12" class="icon icon--phone">
        <rect x="0" y="0" width="12" height="12" rx="2" fill="var(--gold)"/>
        <path d="M4 3 L5 3 L5.6 4.6 L4.9 5.2 Q5.6 6.6 6.8 7.1 L7.4 6.4 L9 7 L9 8 Q8.8 9 7.8 9 Q3.2 8.6 3 4.2 Q3 3.2 4 3 Z" fill="#fff"/>
      </svg>
      <svg viewBox="0 0 12 12" class="icon icon--mail">
        <rect x="0" y="0" width="12" height="12" rx="2" fill="var(--gold)"/>
        <rect x="2.5" y="3.5" width="7" height="5" fill="none" stroke="#fff" stroke-width="0.9"/>
        <path d="M2.5 3.5 L6 6.3 L9.5 3.5" fill="none" stroke="#fff" stroke-width="0.9"/>
      </svg>
      <svg viewBox="0 0 12 12" class="icon icon--web">
        <rect x="0" y="0" width="12" height="12" rx="2" fill="var(--gold)"/>
        <circle cx="6" cy="6" r="3.4" fill="none" stroke="#fff" stroke-width="0.9"/>
        <ellipse cx="6" cy="6" rx="1.4" ry="3.4" fill="none" stroke="#fff" stroke-width="0.7"/>
        <line x1="2.6" y1="6" x2="9.4" y2="6" stroke="#fff" stroke-width="0.7"/>
      </svg>
    </div>
    <ul class="contact-list">
      <li>0493 257618</li>
      <li>tom@tomharvecoaching.com</li>
      <li>www.tomharvecoaching.com</li>
    </ul>
  </section>
</main>
</body>
</html>
```